new service company in the field of construction seeks to make the Creation of a PPT

We need a PPT format with a cover page a frame for presentation. our company is based in Paris which was named VORENTEX. we just did our logo attached. Our company offers services to manage and control documents that pass on projects in construction (building, infrastructure, energy, oil and gas etc. ..). We use internet systems to help us, design must show insurance, quality, and safety. Customers should build any type of works and can not build without the approved documents. These documents go through multiple validations, and vorentex staff seconded on projects, coordinate these processes and documents, quality documents, to ensure that project deadlines are met and project management sees his project developed within the period, through regular reporting. the services offered by our company help ensure the project of building on time, to ensure the project manager visibility on what e will not, and can act accordingly.

Target Market(s)

general contractor of engineering construction or big business masters lumber wholesale real estate investor, project ownership in the construction sector

Industry/Entity Type

Construction

Contact Information for Business Card

carte rectangulaire petite taille (4X6cm env)
horizontale ou verticale
prendre en compte les éléments suivants :
logo
nom de société
adresse postale (4 lignes)
teléphone:
mail
role (ex : directeur)
in the back : La qualité documentaire de vos projets

Font styles to use
Sans Serif

Colors
34a7d7
85cae6
cee9f5
0592cd

Requirements
Must have
• The project should have 2 sliders: slider 1. Cover Page 2. slider for the content of presentations THE GOAL IS TO HAVE A VISUAL IDENTITY ON PPT, MY BUSINESS CARDS AND LETTERS must stay in mind and colors of the logo that joined the design must be clean and recall the seriousness, ease. the design must take into account the page numbers Tag line: the documentary quality of your projects information such as tagline and writes must be modifiable
Nice to have
• would require the presentation of the figure shows concepts or reporting table THE GOAL IS TO HAVE A VISUAL IDENTITY ON PPT, MY BUSINESS CARDS AND LETTERS
Should not have
• not to building or building in the logo

```html
<!DOCTYPE html>
<html lang="en">
<head>
<meta charset="utf-8">
<title>Vorentex – Presentation Template</title>
<link rel="stylesheet" href="https://fonts.googleapis.com/css2?family=Noto+Sans:wght@400;600;700&family=Lato:wght@400;700;900&display=swap">
<style>
  :root {
    --canvas: #c9d3d8;
    --sheet: #f3f3f3;
    --slide: #ffffff;
    --slide-border: #cfd3d6;
    --brand-blue: #2358a8;
    --brand-deep: #1d4f9e;
    --band: #2a5aa6;
    --ink: #2b2b2b;
    --muted: #8a8f93;
    --watermark: #dde3e8;
    --photo-sky-a: #2b2fd9;
    --photo-sky-b: #6f8fe0;
    --photo-rock: #5b4a3c;
    --photo-steel-a: #3b3d3f;
    --photo-steel-b: #a7a9a6;
    --photo-board-a: #2a3236;
    --photo-board-b: #b9c6c6;
  }
  * { margin: 0; padding: 0; box-sizing: border-box; }
  html, body { width: 1200px; height: 1200px; overflow: hidden; }
  body { background: var(--canvas); font-family: "Noto Sans", sans-serif; position: relative; }

  .sorter { position: absolute; left: 50px; top: 54px; width: 1100px; height: 688px; background: var(--sheet); }

  .slide { position: absolute; width: 507px; height: 288px; background: var(--slide);
           border: 1px solid var(--slide-border); overflow: hidden; }
  .slide-label { position: absolute; font-family: "Lato", sans-serif; font-size: 18px; color: var(--muted); }

  .text-slide .copy { position: absolute; left: 0; right: 0; top: 62px; text-align: center;
                      color: var(--brand-blue); font-weight: 600; font-size: 12.4px; line-height: 17px; z-index: 2; }
  .text-slide .copy p { margin-bottom: 15px; }
  .watermark-name { position: absolute; left: 0; right: 0; top: 186px; text-align: center;
                    font-family: "Noto Sans", sans-serif; font-weight: 700; font-size: 82px; line-height: 1;
                    color: var(--watermark); letter-spacing: 1px; z-index: 1; }
  .page-no { position: absolute; font-size: 5px; color: var(--muted); }

  .band { position: absolute; background: var(--band); height: 9px; }
  .band-top { top: 3px; }
  .band-bottom { bottom: 3px; }
  .page-dot { position: absolute; bottom: 1px; width: 11px; height: 11px; border-radius: 50%;
              background: #fff; border: 1px solid var(--band); font-size: 5px; text-align: center; line-height: 9px; color: var(--muted); }

  .slide-title { position: absolute; font-family: "Lato", sans-serif; font-size: 13px; color: var(--ink); letter-spacing: 0.2px; }
  .slide-subtitle { position: absolute; font-size: 5.5px; color: var(--brand-blue); }
  .brand-name { position: absolute; font-family: "Noto Sans", sans-serif; font-weight: 700; font-size: 14px;
                color: var(--brand-deep); letter-spacing: 0.2px; }

  .photo { position: absolute; }
  .photo-climb { left: 2px; top: 2px; width: 192px; height: 284px;
                 background: linear-gradient(160deg, var(--photo-sky-a) 0%, var(--photo-sky-b) 55%, var(--photo-rock) 100%); }
  .photo-gears { left: 29px; top: 66px; width: 216px; height: 138px;
                 background: linear-gradient(120deg, var(--photo-steel-a), var(--photo-steel-b) 60%, #8a7440); }
  .photo-board { left: 259px; top: 66px; width: 220px; height: 138px;
                 background: linear-gradient(120deg, var(--photo-board-a), var(--photo-board-b)); }

  .bullets { position: absolute; left: 213px; top: 144px; width: 232px; list-style: none; }
  .bullets li { position: relative; padding-left: 14px; font-size: 6.6px; line-height: 10px; color: var(--ink); margin-bottom: 12px; }
  .bullets li::before { content: ""; position: absolute; left: 2px; top: 3.5px; width: 3px; height: 3px; border-radius: 50%; background: var(--brand-blue); }

  .caption { position: absolute; top: 213px; width: 212px; font-size: 5.4px; line-height: 8.4px; color: #555; }
</style>
</head>
<body>
  <main class="sorter">
    <!-- Slide 3 -->
    <section class="slide text-slide" style="left:21px; top:20px;">
      <div class="copy">
        <p>Lorem ipsum dolor sit amet, consetetur sadipscing elitr, sed diam<br>nonumy eirmod tempor invidunt ut labore et dolore magna<br>aliquyam erat, sed diam voluptua. At vero eos et accusam</p>
        <p>Lorem ipsum dolor sit amet, consetetur sadipscing elitr, sed diam<br>nonumy eirmod tempor invidunt ut labore et dolore magna<br>aliquyam erat, sed diam voluptua. At vero eos et accusam</p>
        <p>Lorem ipsum dolor sit amet, consetetur sadipscing elitr, sed diam<br>nonumy eirmod tempor invidunt ut labore et dolore magna<br>aliquyam erat, sed diam voluptua. At vero eos et accusam</p>
      </div>
      <span class="page-no" style="left:460px; top:268px;">3</span>
    </section>
    <span class="slide-label" style="left:24px; top:318px;">3</span>

    <!-- Slide 4 -->
    <section class="slide text-slide" style="left:564px; top:20px;">
      <div class="watermark-name">VORENTEX</div>
      <div class="copy">
        <p>Lorem ipsum dolor sit amet, consetetur sadipscing elitr, sed diam<br>nonumy eirmod tempor invidunt ut labore et dolore magna<br>aliquyam erat, sed diam voluptua. At vero eos et accusam</p>
        <p>Lorem ipsum dolor sit amet, consetetur sadipscing elitr, sed diam<br>nonumy eirmod tempor invidunt ut labore et dolore magna<br>aliquyam erat, sed diam voluptua. At vero eos et accusam</p>
        <p>Lorem ipsum dolor sit amet, consetetur sadipscing elitr, sed diam<br>nonumy eirmod tempor invidunt ut labore et dolore magna<br>aliquyam erat, sed diam voluptua. At vero eos et accusam</p>
      </div>
      <span class="page-no" style="left:460px; top:268px;">4</span>
    </section>
    <span class="slide-label" style="left:567px; top:318px;">4</span>

    <!-- Slide 5 -->
    <section class="slide" style="left:21px; top:372px;">
      <div class="photo photo-climb" role="img" aria-label="Photo of two climbers helping each other up a rock against a bright blue sky"></div>
      <div class="band band-top" style="left:194px; right:3px;"></div>
      <h2 class="slide-title" style="left:206px; top:24px;">LOREM IPSUM DOLOR SIT AMET</h2>
      <p class="slide-subtitle" style="left:206px; top:42px;">Lorem ipsum dolor sit amet</p>
      <span class="brand-name" style="left:418px; top:32px;">VORENTEX</span>
      <ul class="bullets">
        <li>Lorem ipsum dolor sit amet, consetetur sadipscing elitr, sed diam nonumy eirmod tempor invidunt ut labore et dolore magna aliquyam erat, sed diam voluptua. At vero eos et accusam</li>
        <li>Lorem ipsum dolor sit amet, consetetur sadipscing elitr, sed diam nonumy eirmod tempor invidunt ut labore et dolore magna aliquyam erat, sed diam voluptua. At vero eos et accusam</li>
        <li>Lorem ipsum dolor sit amet, consetetur sadipscing elitr, sed diam nonumy eirmod tempor invidunt ut labore et dolore magna aliquyam erat, sed diam voluptua. At vero eos et accusam</li>
      </ul>
      <div class="band band-bottom" style="left:194px; right:3px;"></div>
      <span class="page-dot" style="left:452px;">5</span>
    </section>
    <span class="slide-label" style="left:24px; top:670px;">5</span>

    <!-- Slide 6 -->
    <section class="slide" style="left:564px; top:372px;">
      <div class="band band-top" style="left:3px; right:3px;"></div>
      <h2 class="slide-title" style="left:31px; top:24px;">LOREM IPSUM DOLOR SIT AMET</h2>
      <p class="slide-subtitle" style="left:31px; top:42px;">Lorem ipsum dolor sit amet</p>
      <span class="brand-name" style="left:418px; top:32px;">VORENTEX</span>
      <div class="photo photo-gears" role="img" aria-label="Close-up photo of industrial gears and shafts"></div>
      <div class="photo photo-board" role="img" aria-label="Close-up photo of a hand placing a component on a circuit board"></div>
      <p class="caption" style="left:29px;">Lorem ipsum dolor sit amet, consetetur sadipscing elitr, sed diam nonumy eirmod tempor invidunt ut labore et dolore magna aliquyam erat, sed diam voluptua. At vero eos et accusam et justo duo dolores et ea rebum. Stet clita kasd gubergren, no sea takimata sanctus est</p>
      <p class="caption" style="left:259px;">Lorem ipsum dolor sit amet, consetetur sadipscing elitr, sed diam nonumy eirmod tempor invidunt ut labore et dolore magna aliquyam erat, sed diam voluptua. At vero eos et accusam et justo duo dolores et ea rebum. Stet clita kasd gubergren, no sea takimata sanctus est</p>
      <div class="band band-bottom" style="left:3px; right:3px;"></div>
      <span class="page-dot" style="left:452px;">6</span>
    </section>
    <span class="slide-label" style="left:567px; top:670px;">6</span>
  </main>
</body>
</html>
```